依頼詳細
【依頼内容】
ネットプリントのテンプレートとして使用する「A4仕上がりの2つ折りパンフレット(両面)」のデザインをご提案ください。
複数当選(最大10点)を予定しておりますので、ご応募は両面で1点ずつお願いいたします。
お一人様で何点でもご応募いただけます。

下のURLは名刺デザインになりますが、
これの「2つ折りパンフレット」と想定してください。
https://qovlprint.net/order/design/ondemand/businesscard.html?products_id=1

他社様ですが このようなパンフレットデザインをイメージしております。
https://design.fenvimo.com/products/pamphlet

【デザインの要望】
・主に会社案内・施設紹介・商品紹介などのデザインを想定しております。
・どのデザインも汎用性のあるデザインをお願いいたします。

【サイズ詳細】
作成サイズ 420mm×297mm 350dpi(CMYKカラー)
添付の「作成用テンプレート」をご利用いただけます。
※作成用テンプレートの利用は任意です。ご利用いただかなくても問題ございません。

【書体について】
お客様が編集すると想定している部分などは
編集可能文字になりますので、使用書体に制限がございます。

■使用可能な書体はこちらでご確認いただけます。
https://qovlprint.net/guide/design-entry.html

背景になる固定の文字などの書体に制限はございません。
お好みの書体をご使用ください。

【報酬について】
報酬は採用=42,000円、入選=41,000円を予定しておりますが、
この金額にはシステム利用料金・消費税が含まれております。
実際には 40,000円からシステム手数料・消費税などを引いた金額が報酬金額になります。
ご注意ください。

【利用用途】
弊社Webサイトから発注できるテンプレートとして利用させていただきます。
2つ折りパンフレット以外にもデザインテンプレートとして
利用させていただく場合がございます。
サイズ
A4
ページ数
4ページ
希望イメージ
• +5 0 +5
• シンプル
複雑
• 単色
カラフル
• 暗い
明るい
• 日常
高級
• 遊び心
厳粛
• 未来的
伝統的
• 女性的
男性的
希望する色
納品ファイル
• イラストレーター形式 (.ai)
補足説明
納品後、弊社で編集する場合がございますので、編集可能なデータ作成をお願いいたします。
依頼公開後の追記内容
■ 選んだ理由

とても素敵なデザインばかりで選考がとても難しかったですが、写真の並びや説明文がテンプレートとしてユーザーに使いやすく、目を引き興味を持ってもらえるデザインを選ばせていただきました。
素晴らしいデザインをご提案いただき誠にありがとうございました。

■ 提案者全員のお礼・コメント

この度は素晴らしいご提案多数いただき誠にありがとうございました。
とても素敵で目を引くデザインが多く、社内選考でもかなり意見が割れ選考がとても難しかったですが今回は初めて2つ折りパンフレットのテンプレートを用意するという点でユーザーにとって使いやすいデザインを選ばせていただきました。

弊社では今後もテンプレートを充実させていくべく、様々なデザインの募集を行う予定でございます。
その際にはまた是非ご提案いただけますと幸いです。
今後とも何卒よろしくお願い申しあげます。

```html
<!DOCTYPE html>
<html lang="ja">
<head>
<meta charset="utf-8">
<title>とんかつ 折パンフレット</title>
<link rel="stylesheet" href="https://fonts.googleapis.com/css2?family=Noto+Sans+JP:wght@400;700;900&family=Noto+Serif+JP:wght@700;900&family=Yuji+Syuku&display=swap">
<style>
:root{
  --red:#c8161d;
  --red-dark:#a30f15;
  --green:#1f7a3a;
  --ink:#1a1a1a;
  --grey:#666;
  --cream:#f3e7d3;
  --paper:#ffffff;
  --line:#bdbdbd;
  --logo-yellow:#e7b400;
}
*{box-sizing:border-box;margin:0;padding:0}
html,body{width:726px;height:1200px;overflow:hidden;background:#fff}
body{position:relative;font-family:"Noto Sans JP",sans-serif;color:var(--ink)}
.abs{position:absolute}
.sheet-head{position:absolute;left:6px;height:44px;width:714px;display:flex;align-items:center;gap:10px}
.brand{display:flex;align-items:center;gap:5px;font-weight:900;font-size:14px;color:var(--ink)}
.brand-mark{width:14px;height:14px;background:var(--logo-yellow)}
.sheet-title{font-weight:700;font-size:12px}
.sheet-note{font-size:7px;color:var(--grey);line-height:1.3}
.fold-label{position:absolute;left:0;width:726px;text-align:center;font-size:8px;color:var(--grey)}
.spread{position:absolute;left:50px;width:662px;background:var(--paper);box-shadow:0 0 0 1px #ddd;overflow:hidden}
.fold{position:absolute;left:331px;top:0;bottom:0;border-left:1px dashed #ccc}
.band{position:absolute;left:0;right:0;background:var(--red)}
.photo{position:absolute;border-radius:4px}
/* front */
.front-right{position:absolute;left:331px;top:0;width:331px;height:100%;background:linear-gradient(#fff 40%,var(--cream))}
.front-left{position:absolute;left:0;top:0;width:331px;height:100%;background:linear-gradient(#fff 55%,#f6efe4)}
.shop-title{font-family:"Noto Serif JP",serif;font-weight:900;font-size:34px;line-height:1}
.shop-sub{font-family:"Noto Serif JP",serif;font-weight:900;font-size:24px;letter-spacing:4px;line-height:1}
.catch{writing-mode:vertical-rl;font-family:"Yuji Syuku",serif;font-size:26px;color:var(--red);line-height:1.3}
.catch em{font-style:normal;font-size:40px}
.hours{display:flex;align-items:center;gap:6px;font-size:10px;font-weight:700}
.hours-tag{background:var(--red);color:#fff;padding:3px 6px}
.hours-text{border-bottom:2px solid var(--red);padding:2px 4px}
.tel{font-weight:900;font-size:28px;color:var(--red-dark);letter-spacing:1px}
.addr{font-size:7px;color:var(--grey)}
.set-title{font-size:11px;font-weight:700;color:var(--red)}
.set-item{position:absolute;width:70px;text-align:center}
.set-item .photo{position:static;display:block;width:70px;height:56px}
.set-label{font-size:10px;font-weight:700;margin-top:4px}
.set-label b{color:var(--red);font-size:13px}
/* back */
.menu-pill{position:absolute;height:26px;border-radius:13px;color:#fff;font-weight:700;font-size:13px;display:flex;align-items:center;justify-content:center}
.pill-red{background:var(--red)}
.pill-green{background:var(--green)}
.col-head{position:absolute;font-size:10px;font-weight:700}
.menu-list{position:absolute;list-style:none}
.menu-list li{display:flex;align-items:baseline;font-size:11px;border-bottom:1px dotted var(--line);height:var(--row)}
.menu-list .name{flex:1;padding-top:12px}
.menu-list .price{width:84px;text-align:right;font-size:9px}
.frame{position:absolute;border:1px solid var(--line)}
.caption{font-size:8px;color:var(--grey)}
</style>
</head>
<body>

<header class="sheet-head" style="top:0">
  <div class="brand"><span class="brand-mark"></span>QOVLPRINT</div>
  <div class="sheet-title">折パンフ_A4_表面</div>
  <div class="sheet-note">※ページ(1・4P)<br>仕上サイズ 420×297mm 塗足し3mm</div>
</header>
<div class="fold-label" style="top:44px">センターで山折り</div>

<section class="spread" style="top:58px;height:490px">
  <div class="front-left">
    <svg class="abs" style="left:130px;top:170px" width="70" height="70" viewBox="0 0 70 70" role="img" aria-label="配達アイコン">
      <rect x="1.5" y="1.5" width="67" height="67" rx="10" fill="#fff" stroke="var(--red)" stroke-width="3"/>
      <rect x="12" y="22" width="28" height="22" fill="var(--red)"/>
      <path d="M40 28h10l7 8v8H40z" fill="var(--red)"/>
      <circle cx="22" cy="48" r="5" fill="var(--red)" stroke="#fff" stroke-width="2"/>
      <circle cx="48" cy="48" r="5" fill="var(--red)" stroke="#fff" stroke-width="2"/>
    </svg>
    <div class="set-title abs" style="left:20px;top:340px">お得なセットメニュー</div>
    <div class="set-item" style="left:22px;top:360px">
      <div class="photo" role="img" aria-label="B弁当の写真" style="background:linear-gradient(135deg,#d59a4a,#8a5a2b)"></div>
      <div class="set-label">B弁当 <b>¥750</b></div>
    </div>
    <div class="set-item" style="left:122px;top:360px">
      <div class="photo" role="img" aria-label="B弁当の写真" style="background:linear-gradient(135deg,#e0a85a,#7d4e24)"></div>
      <div class="set-label">B弁当 <b>¥840</b></div>
    </div>
    <div class="set-item" style="left:222px;top:360px">
      <div class="photo" role="img" aria-label="C弁当の写真" style="background:linear-gradient(135deg,#d8a052,#86552a)"></div>
      <div class="set-label">C弁当 <b>¥945</b></div>
    </div>
  </div>

  <div class="front-right">
    <div class="photo" role="img" aria-label="とんかつと千切りキャベツの写真" style="left:14px;top:96px;width:222px;height:220px;border-radius:6px;background:linear-gradient(160deg,#eef0d6 0%,#d9a55a 45%,#a8642a 75%,#3a2a20 100%)"></div>
    <div class="shop-title abs" style="left:24px;top:24px">とんかつ</div>
    <div class="shop-sub abs" style="left:44px;top:68px">○○○○</div>
    <div class="catch abs" style="left:244px;top:22px;height:300px">専門店の<em>味</em>を<br>お届けします。</div>
    <div class="hours abs" style="left:10px;top:338px">
      <span class="hours-tag">配達時間</span>
      <span class="hours-text">昼/11：30～14：00　夜/17：30～20：30</span>
    </div>
    <div class="tel abs" style="left:14px;top:364px">TEL 000-000-0000</div>
    <div class="addr abs" style="left:16px;top:404px">〒000-0000 ○○県○○市○○町0-0-0 定休日 水曜</div>
  </div>
  <div class="fold"></div>
  <div class="band" style="top:456px;height:34px"></div>
  <div class="band" style="top:450px;height:2px"></div>
</section>

<header class="sheet-head" style="top:558px">
  <div class="brand"><span class="brand-mark"></span>QOVLPRINT</div>
  <div class="sheet-title">折パンフ_A4_裏面</div>
  <div class="sheet-note">※ページ(2・3P)<br>仕上サイズ 420×297mm 塗足し3mm</div>
</header>
<div class="fold-label" style="top:602px">センターで山折り</div>

<section class="spread" style="top:616px;height:574px">
  <div class="band" style="top:0;height:14px"></div>
  <div class="band" style="bottom:0;height:14px"></div>

  <div class="menu-pill pill-red" style="left:60px;top:40px;width:130px">とんかつ</div>
  <div class="col-head" style="left:206px;top:62px">一品</div>
  <div class="col-head" style="left:286px;top:62px;color:var(--red)">弁当</div>
  <ul class="menu-list" style="left:28px;top:76px;width:280px;--row:40px">
    <li><span class="name">ヒレかつ</span><span class="price">0,000円</span><span class="price">0,000円</span></li>
    <li><span class="name">ロースかつ</span><span class="price">0,000円</span><span class="price">0,000円</span></li>
    <li><span class="name">えびフライ</span><span class="price">0,000円</span><span class="price">0,000円</span></li>
    <li><span class="name">チキンかつ</span><span class="price">0,000円</span><span class="price">0,000円</span></li>
    <li><span class="name">串かつ</span><span class="price">0,000円</span><span class="price">0,000円</span></li>
    <li><span class="name">ひとくちヒレかつ</span><span class="price">0,000円</span><span class="price">0,000円</span></li>
  </ul>
  <div class="photo" role="img" aria-label="キャベツの写真" style="left:46px;top:380px;width:86px;height:70px;background:linear-gradient(135deg,#e9ecc9,#b9c68a)"></div>
  <div class="photo" role="img" aria-label="みそ汁の写真" style="left:142px;top:380px;width:86px;height:70px;background:linear-gradient(135deg,#cfa772,#6a4a2a)"></div>
  <div class="caption abs" style="left:46px;top:462px">お弁当にはキャベツとみそ汁が付きます。</div>

  <div class="fold"></div>

  <div class="frame" style="left:350px;top:36px;width:290px;height:500px"></div>
  <div class="menu-pill pill-green" style="left:432px;top:42px;width:120px">かつ重</div>
  <div class="col-head" style="left:590px;top:68px;color:var(--red)">弁当</div>
  <ul class="menu-list" style="left:368px;top:82px;width:256px;--row:38px">
    <li><span class="name">ロースかつ重</span><span class="price">0,000円</span></li>
    <li><span class="name">えび重</span><span class="price">0,000円</span></li>
    <li><span class="name">ヒレかつ重</span><span class="price">0,000円</span></li>
    <li><span class="name">えびヒレかつ重</span><span class="price">0,000円</span></li>
  </ul>
  <div class="menu-pill pill-green" style="left:432px;top:252px;width:120px">サイドメニュー</div>
  <ul class="menu-list" style="left:368px;top:290px;width:256px;--row:34px">
    <li><span class="name">ポテトサラダ</span><span class="price">000円</span></li>
    <li><span class="name">千切りキャベツ</span><span class="price">000円</span></li>
    <li><span class="name">自家製みそ汁</span><span class="price">000円</span></li>
    <li><span class="name">お新香</span><span class="price">000円</span></li>
    <li><span class="name">ライス</span><span class="price">000円</span></li>
  </ul>
</section>

</body>
</html>
```